Präsentationsvorlagen
Zielgruppe
Die velora systems GmbH ist ein kleines Beratungsunternehmen mit drei Beratern, das sich auf Brightwell 365-Beratung spezialisiert hat. Das Unternehmen bietet Dienstleistungen in den Bereichen Security, Compliance und Device Management an, insbesondere mit Brightwell Keystra.
Darüber hinaus entwickelt velora systems das SaaS-Produkt 'Tandemo', das überprüft, ob ein B365-Tenant sicher konfiguriert ist. Tandemo basiert auf eigenen Best Practices und wird durch ein Rechtsgutachten ergänzt, um die Sicherheit eines Tenants auch aus juristischer Sicht zu bewerten.
Zielgruppe von velora systems
IT-Leiter und IT-Administratoren, die für Brightwell 365 und Security verantwortlich sind
Unternehmen, die Brightwell Keystra für ihre Geräteverwaltung einsetzen oder dies planen
IT-Dienstleister, die Security- und Compliance-Anforderungen für ihre Kunden umsetzen müssen
Krankenkassen und andere regulierte Branchen, die eine sichere und gesetzeskonforme B365-Umgebung benötigen
Aufgabenstellung
1. General Design & Functional Principles
1.1 Corporate Identity (CI) Integration
All templates must use the company’s branding (colors, fonts, logos, spacing).
Ensure that SmartArt, shapes, tables, and lists automatically adopt the branded theme when newly created.
1.2 Print & PDF Export Compatibility
Templates must translate well into A4-sized PDFs and remain visually consistent in print.
Avoid distortions when exporting or printing.
1.3 Accessibility & Readability
Maintain high contrast and readable font sizes.
Alternative text must be included for all images and media.
Support for screen readers and keyboard navigation must be ensured across all templates.
1.4 AI & Pathmate Optimization
Placeholders should include AI-friendly prompts, such as:
'Summarize this section in one sentence.'
'List three key takeaways from this slide.'
'Rewrite this paragraph at a C-suite level.'
'Generate an executive summary.'
'Provide a bulleted version of this paragraph.'
Naming conventions for placeholders should follow a structured format for AI reference, e.g.:
Executive_Summary_Box
Decision_Options_Table
Key_Takeaways_List
1.5 Flexible Content Accommodation
List-based content must support short and long variants (e.g., 3-5 items, 6-10 items).
1.6 Default Theme for Newly Created Elements
Ensure that default tables, charts, SmartArt, and shapes adopt the corporate theme.
Layouts:
Title Slide (Introduction & Branding)
Sets the stage for the presentation by introducing the topic, presenter, and company.
Includes: Main title, subtitle, company logo, and optional background image.
Agenda Slide (Navigation & Structure)
Provides an overview of the key topics and sections to help the audience follow along.
Includes: A clear agenda list (short or extended), optional icons for visual appeal.
Section Header Slide (Transitions & ..

```html
<!DOCTYPE html>
<html lang="de">
<head>
<meta charset="utf-8">
<title>Präsentationsvorlagen – Folienübersicht</title>
<link rel="stylesheet" href="https://fonts.googleapis.com/css2?family=Archivo:wght@700;800&family=Carlito:ital,wght@0,400;1,400&family=Roboto:wght@400&display=swap">
<style>
  :root {
    --page-bg: #ffffff;
    --slide-bg: #fdfdfb;
    --slide-bar: #1c1c1c;
    --olive: #b7b800;
    --ink: #1a1a1a;
    --title-gray: #555555;
    --grid: #e3e3e3;
    --axis-text: #666666;
    --purple: #7030a0;
    --orange: #ed7d31;
    --blue: #0070c0;
    --black: #1a1a1a;
    --red: #ff0000;
    --navy: #0b2566;
    --steel: #1f5f8b;
    --forest: #1e6b2a;
    --green: #00b050;
    --bar-green: #00a650;
    --lime: #c0c000;
    --line-navy: #1f4e79;
    --hex-edge: #9a9a9a;
  }
  * { margin: 0; padding: 0; box-sizing: border-box; }
  html, body { width: 1200px; height: 2590px; overflow: hidden; background: var(--page-bg); }
  .sheet { position: relative; width: 1200px; height: 2590px; }
  .slide {
    position: absolute; left: 120px; width: 960px; height: 540px;
    background: var(--slide-bg);
    box-shadow: 0 14px 34px rgba(0,0,0,0.28);
    border-bottom: 7px solid var(--slide-bar);
    overflow: hidden;
  }
  .slide--agenda { top: 96px; }
  .slide--yearly { top: 736px; }
  .slide--product { top: 1336px; }
  .slide--timeline { top: 1940px; }
  .slide svg.art { position: absolute; left: 0; top: 0; }

  .agenda-title {
    position: absolute; left: 65px; top: 36px;
    font-family: "Archivo", Arial, sans-serif; font-weight: 800;
    font-size: 31px; letter-spacing: 0.5px; color: var(--olive);
  }
  .agenda-rule { position: absolute; left: 65px; top: 74px; width: 176px; height: 7px; background: var(--ink); }
  .agenda-intro {
    position: absolute; left: 65px; top: 115px;
    font-family: "Carlito", Calibri, sans-serif; font-style: italic; font-size: 13.5px; color: var(--ink);
  }
  .note {
    position: absolute; width: 340px;
    font-family: "Carlito", Calibri, sans-serif; font-style: italic; font-size: 13.5px; line-height: 19px; color: var(--ink);
  }
  .note--narrow { width: 225px; }

  .chart-title { font-family: "Archivo", Arial, sans-serif; font-weight: 700; fill: var(--title-gray); }
  .axis-label { font-family: "Roboto", Arial, sans-serif; font-size: 10px; fill: var(--axis-text); }
  .legend-label { font-family: "Roboto", Arial, sans-serif; font-size: 10px; fill: var(--axis-text); }

  .product-divider { position: absolute; left: 520px; top: 124px; width: 4px; height: 300px; background: var(--olive); }

  .tl-text { font-family: "Roboto", Arial, sans-serif; font-size: 16px; }
</style>
</head>
<body>
<main class="sheet">

  <section class="slide slide--agenda" aria-label="Agenda">
    <h1 class="agenda-title">AGENDAS</h1>
    <div class="agenda-rule"></div>
    <p class="agenda-intro">These are our agendas, we talk about these topics in detail in this presentation. A dummy text ends here.</p>

    <svg class="art" width="960" height="540" viewBox="0 0 960 540" aria-hidden="true">
      <defs>
        <polygon id="hex-agenda" points="-9,-16 9,-16 18,0 9,16 -9,16 -18,0"/>
      </defs>
      <g transform="translate(63,210)"><use href="#hex-agenda" x="4" fill="var(--hex-edge)"/><use href="#hex-agenda" fill="var(--purple)"/></g>
      <g transform="translate(510,210)"><use href="#hex-agenda" x="4" fill="var(--hex-edge)"/><use href="#hex-agenda" fill="var(--orange)"/></g>
      <g transform="translate(63,323)"><use href="#hex-agenda" x="4" fill="var(--hex-edge)"/><use href="#hex-agenda" fill="var(--blue)"/></g>
      <g transform="translate(510,323)"><use href="#hex-agenda" x="4" fill="var(--hex-edge)"/><use href="#hex-agenda" fill="var(--black)"/></g>
      <g transform="translate(63,443)"><use href="#hex-agenda" x="4" fill="var(--hex-edge)"/><use href="#hex-agenda" fill="var(--red)"/></g>
      <g transform="translate(510,443)"><use href="#hex-agenda" x="4" fill="var(--hex-edge)"/><use href="#hex-agenda" fill="var(--navy)"/></g>
    </svg>

    <p class="note" style="left:112px;top:191px">These are our agendas, we talk about these topics<br>in detail in this presentation. A dummy<br>Text ends here.</p>
    <p class="note" style="left:559px;top:191px">These are our agendas, we talk about these topics<br>in detail in this presentation. A dummy<br>Text ends here.</p>
    <p class="note" style="left:112px;top:304px">These are our agendas, we talk about these topics<br>in detail in this presentation. A dummy<br>Text ends here.</p>
    <p class="note" style="left:559px;top:304px">These are our agendas, we talk about these topics<br>in detail in this presentation. A dummy<br>Text ends here.</p>
    <p class="note" style="left:112px;top:424px">These are our agendas, we talk about these topics<br>in detail in this presentation. A dummy<br>Text ends here.</p>
    <p class="note" style="left:559px;top:424px">These are our agendas, we talk about these topics<br>in detail in this presentation. A dummy<br>Text ends here.</p>
  </section>

  <section class="slide slide--yearly" aria-label="Yearly chart">
    <svg class="art" width="960" height="540" viewBox="0 0 960 540" role="img" aria-label="Bar chart of yearly profit and loss, 2019 to 2021 repeated three times">
      <text class="chart-title" x="480" y="75" font-size="19" text-anchor="middle">YEARLY CHART</text>
      <g stroke="var(--grid)" stroke-width="1">
        <line x1="186" y1="95" x2="792" y2="95"/><line x1="186" y1="129" x2="792" y2="129"/>
        <line x1="186" y1="163" x2="792" y2="163"/><line x1="186" y1="197" x2="792" y2="197"/>
        <line x1="186" y1="231" x2="792" y2="231"/><line x1="186" y1="265" x2="792" y2="265"/>
        <line x1="186" y1="298" x2="792" y2="298"/><line x1="186" y1="332" x2="792" y2="332"/>
        <line x1="186" y1="366" x2="792" y2="366"/><line x1="186" y1="400" x2="792" y2="400"/>
        <line x1="186" y1="434" x2="792" y2="434" stroke="#cfcfcf"/>
      </g>
      <g class="axis-label" text-anchor="end">
        <text x="176" y="98">5</text><text x="176" y="132">4.5</text><text x="176" y="166">4</text>
        <text x="176" y="200">3.5</text><text x="176" y="234">3</text><text x="176" y="268">2.5</text>
        <text x="176" y="301">2</text><text x="176" y="335">1.5</text><text x="176" y="369">1</text>
        <text x="176" y="403">0.5</text><text x="176" y="437">0</text>
      </g>
      <g fill="var(--bar-green)">
        <rect x="204" y="142" width="14" height="292"/><rect x="271" y="264" width="14" height="170"/><rect x="338" y="197" width="14" height="237"/>
        <rect x="406" y="142" width="14" height="292"/><rect x="473" y="264" width="14" height="170"/><rect x="540" y="197" width="14" height="237"/>
        <rect x="608" y="142" width="14" height="292"/><rect x="675" y="264" width="14" height="170"/><rect x="742" y="197" width="14" height="237"/>
      </g>
      <g fill="var(--black)">
        <rect x="223" y="271" width="14" height="163"/><rect x="290" y="136" width="14" height="298"/><rect x="357" y="312" width="14" height="122"/>
        <rect x="425" y="271" width="14" height="163"/><rect x="492" y="136" width="14" height="298"/><rect x="559" y="312" width="14" height="122"/>
        <rect x="627" y="271" width="14" height="163"/><rect x="694" y="136" width="14" height="298"/><rect x="761" y="312" width="14" height="122"/>
      </g>
      <g class="axis-label" text-anchor="middle">
        <text x="221" y="453">2019</text><text x="288" y="453">2020</text><text x="355" y="453">2021</text>
        <text x="423" y="453">2019</text><text x="490" y="453">2020</text><text x="557" y="453">2021</text>
        <text x="625" y="453">2019</text><text x="692" y="453">2020</text><text x="759" y="453">2021</text>
      </g>
      <rect x="440" y="470" width="7" height="7" fill="var(--bar-green)"/>
      <text class="legend-label" x="450" y="477">Profit</text>
      <rect x="487" y="470" width="7" height="7" fill="var(--black)"/>
      <text class="legend-label" x="497" y="477">Loss</text>
    </svg>
  </section>

  <section class="slide slide--product" aria-label="Product report">
    <svg class="art" width="960" height="540" viewBox="0 0 960 540" role="img" aria-label="Line chart of three products from 2021 to 2024">
      <text class="chart-title" x="262" y="172" font-size="19" text-anchor="middle">PRODUCT REPORT</text>
      <g stroke="var(--grid)" stroke-width="1">
        <line x1="101" y1="193" x2="445" y2="193"/><line x1="101" y1="219" x2="445" y2="219"/>
        <line x1="101" y1="244" x2="445" y2="244"/><line x1="101" y1="270" x2="445" y2="270"/>
        <line x1="101" y1="296" x2="445" y2="296"/><line x1="101" y1="321" x2="445" y2="321"/>
        <line x1="101" y1="347" x2="445" y2="347" stroke="#cfcfcf"/>
      </g>
      <g class="axis-label" text-anchor="end">
        <text x="90" y="196">6</text><text x="90" y="222">5</text><text x="90" y="247">4</text>
        <text x="90" y="273">3</text><text x="90" y="299">2</text><text x="90" y="324">1</text><text x="90" y="350">0</text>
      </g>
      <g class="axis-label" text-anchor="middle">
        <text x="142" y="368">2021</text><text x="227" y="368">2022</text><text x="313" y="368">2023</text><text x="398" y="368">2024</text>
      </g>
      <g fill="none" stroke-width="2">
        <polyline stroke="var(--line-navy)" points="142,237 227,283 313,257 398,231"/>
        <polyline stroke="var(--orange)" points="142,285 227,234 313,301 398,275"/>
        <polyline stroke="var(--forest)" points="142,296 227,296 313,270 398,219"/>
      </g>
      <line x1="142" y1="386" x2="162" y2="386" stroke="var(--line-navy)" stroke-width="2"/>
      <text class="legend-label" x="165" y="389">Product 1</text>
      <line x1="228" y1="386" x2="248" y2="386" stroke="var(--orange)" stroke-width="2"/>
      <text class="legend-label" x="251" y="389">Product 2</text>
      <line x1="314" y1="386" x2="334" y2="386" stroke="var(--forest)" stroke-width="2"/>
      <text class="legend-label" x="337" y="389">Product 3</text>

      <defs>
        <polygon id="hex-note" points="-9,-17 9,-17 18,0 9,17 -9,17 -18,0"/>
      </defs>
      <g transform="translate(607,146)"><use href="#hex-note" x="4" fill="var(--hex-edge)"/><use href="#hex-note" fill="var(--orange)"/></g>
      <g transform="translate(607,264)"><use href="#hex-note" x="4" fill="var(--hex-edge)"/><use href="#hex-note" fill="var(--steel)"/></g>
      <g transform="translate(607,390)"><use href="#hex-note" x="4" fill="var(--hex-edge)"/><use href="#hex-note" fill="var(--forest)"/></g>
    </svg>
    <div class="product-divider"></div>
    <p class="note note--narrow" style="left:648px;top:128px">These are our agendas, we talk<br>about these topics in detail in this<br>presentation. A dummy<br>Text ends here.</p>
    <p class="note note--narrow" style="left:648px;top:246px">These are our agendas, we talk<br>about these topics in detail in this<br>presentation. A dummy<br>Text ends here.</p>
    <p class="note note--narrow" style="left:648px;top:371px">These are our agendas, we talk<br>about these topics in detail in this<br>presentation. A dummy<br>Text ends here.</p>
  </section>

  <section class="slide slide--timeline" aria-label="Timeline 2019 to 2024">
    <svg class="art" width="960" height="540" viewBox="0 0 960 540" role="img" aria-label="Timeline from 2019 to 2024">
      <defs>
        <polygon id="hex-outer" points="0,-46 40,-23 40,23 0,46 -40,23 -40,-23"/>
        <polygon id="hex-inner" points="0,-36 31,-18 31,18 0,36 -31,18 -31,-18"/>
        <marker id="arrowhead" markerWidth="8" markerHeight="8" refX="7" refY="4" orient="auto">
          <path d="M0,0 L8,4 L0,8 Z" fill="#444"/>
        </marker>
      </defs>
      <g stroke="#555" stroke-width="1">
        <line x1="154" y1="270" x2="220" y2="270"/>
        <line x1="300" y1="270" x2="367" y2="270"/>
        <line x1="447" y1="270" x2="513" y2="270"/>
        <line x1="593" y1="270" x2="660" y2="270"/>
        <line x1="740" y1="270" x2="804" y2="270" marker-end="url(#arrowhead)"/>
      </g>

      <g transform="translate(114,270)"><use href="#hex-outer" fill="#fff" stroke="var(--blue)" stroke-width="1.5"/><use href="#hex-inner" fill="#f1f1f1"/><circle r="19" fill="var(--blue)"/></g>
      <g transform="translate(260,270)"><use href="#hex-outer" fill="#fff" stroke="var(--purple)" stroke-width="1.5"/><use href="#hex-inner" fill="#f1f1f1"/><circle r="19" fill="var(--purple)"/></g>
      <g transform="translate(407,270)"><use href="#hex-outer" fill="#fff" stroke="var(--orange)" stroke-width="1.5"/><use href="#hex-inner" fill="#f1f1f1"/><circle r="19" fill="var(--orange)"/></g>
      <g transform="translate(553,270)"><use href="#hex-outer" fill="#fff" stroke="var(--red)" stroke-width="1.5"/><use href="#hex-inner" fill="#f1f1f1"/><circle r="19" fill="var(--red)"/></g>
      <g transform="translate(700,270)"><use href="#hex-outer" fill="#fff" stroke="var(--green)" stroke-width="1.5"/><use href="#hex-inner" fill="#f1f1f1"/><circle r="19" fill="var(--green)"/></g>
      <g transform="translate(846,270)"><use href="#hex-outer" fill="#fff" stroke="var(--lime)" stroke-width="1.5"/><use href="#hex-inner" fill="#f1f1f1"/><circle r="19" fill="var(--lime)"/></g>

      <line x1="114" y1="150" x2="114" y2="224" stroke="var(--blue)"/>
      <line x1="407" y1="150" x2="407" y2="224" stroke="var(--orange)"/>
      <line x1="700" y1="150" x2="700" y2="224" stroke="var(--green)"/>
      <line x1="260" y1="316" x2="260" y2="392" stroke="var(--purple)"/>
      <line x1="553" y1="316" x2="553" y2="392" stroke="var(--red)"/>
      <line x1="846" y1="316" x2="846" y2="392" stroke="var(--lime)"/>

      <g class="tl-text" text-anchor="middle">
        <text x="114" y="111" fill="var(--blue)">Dummy Text</text>
        <text x="114" y="133" fill="var(--blue)">Ends Here.</text>
        <text x="407" y="111" fill="var(--orange)">Dummy Text</text>
        <text x="407" y="133" fill="var(--orange)">Ends Here.</text>
        <text x="700" y="111" fill="var(--green)">Dummy Text</text>
        <text x="700" y="133" fill="var(--green)">Ends Here.</text>
        <text x="260" y="425" fill="var(--purple)">Dummy Text</text>
        <text x="260" y="447" fill="var(--purple)">Ends Here.</text>
        <text x="553" y="425" fill="var(--red)">Dummy Text</text>
        <text x="553" y="447" fill="var(--red)">Ends Here.</text>
        <text x="846" y="425" fill="var(--lime)">Dummy Text</text>
        <text x="846" y="447" fill="var(--lime)">Ends Here.</text>

        <text x="112" y="347" fill="var(--blue)">2019</text>
        <text x="264" y="206" fill="var(--purple)">2020</text>
        <text x="410" y="347" fill="var(--orange)">2021</text>
        <text x="552" y="207" fill="var(--red)">2022</text>
        <text x="703" y="345" fill="var(--green)">2023</text>
        <text x="848" y="206" fill="var(--lime)">2024</text>
      </g>
    </svg>
  </section>

</main>
</body>
</html>
```